10-year customer thank you card

We want a greeting card that our sales reps can send to companies/customers who have been with our company for 10 or more years. We're a software company, our corporate color is blue but we also like green, orange, and purple. We'd like something rather minimal/simplistic for this card, perhaps building off our tree logo. We're really open to ideas for this one. You must use the template files that are uploaded. Copy included in 10 year thank you card file; the copy may change based on how it looks when laid out
Updates

I updated our brief. We'd prefer a sans serif font. I also uploaded a blank infographic image that includes more of our approved colors.

Industry/Entity Type

Software

Font styles to use
Sans Serif

```html
<!DOCTYPE html>
<html lang="en">
<head>
<meta charset="utf-8">
<title>Larchfield Software – 10 Years Thank You Card</title>
<link rel="stylesheet" href="https://fonts.googleapis.com/css2?family=Arimo:wght@400;700&display=swap">
<style>
  :root {
    --paper: #f8f8fa;
    --leaf: #8dc344;
    --leaf-shade: #6aa82b;
    --ink: #2b2b2b;
    --rule: #222222;
    --violet: #57349e;
    --violet-deep: #3d1786;
    --white: #ffffff;
  }
  * { margin: 0; padding: 0; box-sizing: border-box; }
  html, body {
    width: 869px;
    height: 1200px;
    overflow: hidden;
    background: var(--paper);
    font-family: "Arimo", Arial, sans-serif;
  }
  .card {
    position: relative;
    width: 869px;
    height: 1200px;
    background: var(--paper);
    overflow: hidden;
  }
  /* Back panel, printed upside down so it reads correctly when folded */
  .back-header {
    position: absolute;
    left: 43px;
    top: 0;
    width: 784px;
    height: 72px;
    transform: rotate(180deg);
    border-top: 2px solid var(--rule);
    display: flex;
    justify-content: space-between;
    align-items: flex-start;
    padding-top: 14px;
  }
  .brand-name {
    display: flex;
    align-items: center;
    gap: 7px;
    font-size: 19px;
    color: var(--ink);
  }
  .brand-mark {
    width: 12px;
    height: 12px;
    background: var(--leaf);
  }
  .web-address {
    font-size: 22px;
    color: var(--leaf);
    letter-spacing: 0.5px;
  }
  /* Front panel */
  .front {
    position: absolute;
    left: 0;
    top: 597px;
    width: 869px;
    height: 603px;
    background: var(--leaf);
    overflow: hidden;
  }
  .front-art {
    position: absolute;
    inset: 0;
  }
  .anniversary-badge {
    position: absolute;
    left: 679px;
    top: 24px;
    width: 158px;
    height: 186px;
    border: 2px solid var(--white);
    color: var(--white);
    text-align: center;
  }
  .anniversary-number {
    display: block;
    font-size: 112px;
    line-height: 1;
    margin-top: 8px;
    letter-spacing: -2px;
  }
  .anniversary-rule {
    display: block;
    width: 140px;
    height: 2px;
    margin: 16px auto 0;
    background: var(--white);
  }
  .anniversary-label {
    display: block;
    font-size: 37px;
    line-height: 1;
    margin-top: 6px;
  }
  .thanks {
    position: absolute;
    left: 0;
    width: 869px;
    top: 462px;
    text-align: center;
    font-size: 66px;
    color: var(--white);
    letter-spacing: -0.5px;
  }
</style>
</head>
<body>
<main class="card">
  <header class="back-header">
    <div class="brand-name"><span class="brand-mark"></span>Larchfield Software</div>
    <div class="web-address">www.larchfield.com</div>
  </header>

  <section class="front">
    <svg class="front-art" width="869" height="603" viewBox="0 0 869 603" aria-hidden="true">
      <!-- long shadows -->
      <polygon fill="var(--leaf-shade)" points="837,24 1000,252 1000,603 900,603 679,210"/>
      <polygon fill="var(--leaf-shade)" points="593,168 900,603 560,603 309,372"/>
      <polygon fill="var(--leaf-shade)" points="300,545 350,545 420,603 370,603"/>
      <polygon fill="var(--leaf-shade)" points="380,545 470,545 540,603 450,603"/>
      <polygon fill="var(--leaf-shade)" points="500,545 605,545 665,603 560,603"/>
      <!-- emblem disc -->
      <circle cx="451" cy="270" r="175" fill="var(--violet)"/>
      <path d="M 571,158 A 175 175 0 0 1 507,436 L 451,366 Z" fill="var(--violet-deep)" opacity="0.55"/>
    </svg>

    <div class="anniversary-badge">
      <span class="anniversary-number">10</span>
      <span class="anniversary-rule"></span>
      <span class="anniversary-label">YEARS</span>
    </div>

    <h1 class="thanks">Thank You</h1>
  </section>
</main>
</body>
</html>
```